HARBOUR LANE DECOR

We need a web design for a new business based in Bonny Hills (NSW). We are a small retail outlet on the Mid North Coast (NSW, Australia) selling home wares, gifts, beach wear, artwork, and hampers etc. We would like to a few different samples if that's not too much trouble (e.g. black and white vs colour, e.g. "beach colours").
We would like the website to communicate that we are an affordable, local (community based) business, with customer satisfaction at the forefront of our mind. We have a strong customer service focus, and in addition to retail sales we are now looking to expand into the online hamper business.
We are open 7 days (except public holidays).
Note: We like the design / layout of the "Cork Pail 'N' Shelf Website" if you would like to compare www.corkpailnshelf.com.au

Industry/Entity Type

Business

```html
<!DOCTYPE html>
<html lang="en">
<head>
<meta charset="utf-8">
<title>Harbour Lane Decor</title>
<link href="https://fonts.googleapis.com/css2?family=Arimo:wght@400;700&display=swap" rel="stylesheet">
<style>
:root{
  --teal:#79cbbd;
  --teal-dark:#5fb8a8;
  --ink:#333;
  --grey:#666;
  --light:#999;
  --panel:#eeeeee;
  --rule:#d6d6d6;
  --white:#fff;
}
*{box-sizing:border-box;margin:0;padding:0}
html,body{width:1200px;height:1000px;overflow:hidden;background:var(--white);font-family:'Arimo',Arial,sans-serif;color:var(--ink)}
.page{position:relative;width:1200px;height:1000px}
.abs{position:absolute}
a{color:inherit;text-decoration:none}

.utility{top:12px;right:156px;font-size:8.5px;color:var(--grey);letter-spacing:.2px}
.utility span{margin:0 3px}

.brand{left:165px;top:46px;font-size:25px;font-weight:700;letter-spacing:1px;color:#222}
.main-nav{top:56px;left:546px;width:498px;display:flex;justify-content:space-between;font-size:10.5px;color:var(--grey);text-transform:uppercase}
.main-nav .active{color:var(--teal-dark)}
.nav-rule{top:78px;left:0;width:1200px;height:4px;background:var(--teal)}

.tagline{left:165px;top:87px;font-size:14.5px;letter-spacing:1.6px;color:#555}
.cart{top:90px;right:156px;display:flex;align-items:center;gap:6px;font-size:12px;color:var(--light)}
.cart .divider{width:1px;height:18px;background:var(--rule);margin:0 4px}

.hero{left:165px;top:113px;width:879px;height:367px;background:radial-gradient(ellipse at 55% 70%,#4a4a48 0%,#1c1c1c 45%,#0d0d0d 100%)}
.dots{left:583px;top:448px;display:flex;gap:5px}
.dots i{width:10px;height:10px;border-radius:50%;background:var(--white)}
.dots i.on{background:var(--teal)}

.tile{top:510px;width:278px;height:131px}
.tile-1{left:165px;background:linear-gradient(135deg,#6f8f84,#8fae9c 50%,#5b6f66)}
.tile-2{left:464px;background:linear-gradient(135deg,#cfd3cf,#e8e6e0 50%,#9aa7a3)}
.tile-3{left:767px;background:linear-gradient(135deg,#5a4436,#a49a92 45%,#dcd8d4)}
.collection{top:659px;width:278px}
.collection h3{font-size:14px;font-weight:400;color:var(--ink)}
.collection p{font-size:11px;color:var(--grey);margin-top:3px}
.collection.featured h3{color:var(--teal-dark)}
.shop-btn{top:661px;width:90px;height:29px;border:1px solid #bbb;font-size:12px;color:var(--grey);display:flex;align-items:center;justify-content:center}
.shop-btn.featured{background:var(--teal);border-color:var(--teal);color:var(--white)}

.newsletter{left:165px;top:738px;width:880px;height:39px;border:1px solid var(--rule);display:flex}
.newsletter .pitch{flex:1;display:flex;align-items:center;padding-left:13px;font-size:11.5px;color:var(--ink)}
.newsletter .pitch strong{font-weight:400;font-size:15px;color:var(--teal-dark);margin-right:4px}
.newsletter .field{width:280px;margin:-1px -1px -1px 0;background:var(--teal);display:flex;align-items:center;justify-content:space-between;padding:0 12px 0 17px;color:var(--white);font-size:8px;font-weight:700}

.perks{left:166px;top:805px;width:878px;display:flex;gap:9px}
.perk{flex:1;height:88px;background:var(--panel);text-align:center;padding-top:22px}
.perk h4{font-size:11px;font-weight:700;letter-spacing:.4px;color:var(--ink)}
.perk p{font-size:10px;line-height:15px;color:var(--grey);margin-top:7px}

.footer-links{left:165px;top:929px;font-size:10px;color:var(--grey)}
.footer-links .current{color:var(--teal-dark);text-decoration:underline}
.footer-links span{margin:0 4px}
.social{top:929px;right:156px;font-size:10px;color:var(--grey)}
.social span{margin:0 4px}
.footer-rule{left:165px;top:952px;width:879px;height:1px;background:var(--rule)}
.legal{left:165px;top:964px;font-size:9.5px;color:var(--grey)}
.payments{top:960px;right:156px;display:flex;gap:3px}
.payments b{width:35px;height:23px;border:1px solid #ccc;border-radius:2px;font-size:7.5px;font-weight:700;color:#555;display:flex;align-items:center;justify-content:center;background:#f7f7f7}
</style>
</head>
<body>
<div class="page">
  <nav class="abs utility">REGISTRATION<span>|</span>LOG IN<span>|</span>DELIVERY<span>|</span>CHECKOUT<span>|</span>MY ACCOUNT</nav>

  <div class="abs brand">HARBOUR LANE DECOR</div>
  <nav class="abs main-nav">
    <a class="active">Home</a><a>About us</a><a>Shop</a><a>Hampers</a><a>Products</a><a>Blog</a><a>Contacts</a>
  </nav>
  <div class="abs nav-rule"></div>

  <div class="abs tagline">homeware. kitchen ware. linen. gifts</div>
  <div class="abs cart">CART
    <svg width="16" height="13" viewBox="0 0 16 13" fill="none" stroke="#aaa" stroke-width="1.3"><path d="M1 4h14l-2 8H3z"/><path d="M5 4l3-3 3 3"/></svg>
    <span class="divider"></span>
    <svg width="14" height="14" viewBox="0 0 14 14" fill="none" stroke="#aaa" stroke-width="1.6"><circle cx="5.5" cy="5.5" r="4"/><path d="M8.5 8.5l4.5 4.5"/></svg>
  </div>

  <div class="abs hero" role="img" aria-label="Barware display: patterned ice buckets, crystal decanters, glasses and wine bottles on a silver tray against a dark wall"></div>
  <div class="abs dots"><i class="on"></i><i></i><i></i></div>

  <div class="abs tile tile-1" role="img" aria-label="Store shelves with ceramic bowls and painted plates"></div>
  <div class="abs tile tile-2" role="img" aria-label="White shelving with patterned cushions and homewares"></div>
  <div class="abs tile tile-3" role="img" aria-label="Wooden cabinet with handbags beside folded linen and cushions"></div>

  <div class="abs collection featured" style="left:166px"><h3>Hamper Collection</h3><p>Shop Hamper Collection</p></div>
  <a class="abs shop-btn featured" style="left:354px">SHOP NOW</a>
  <div class="abs collection" style="left:464px"><h3>Hamper Collection</h3><p>Shop Hamper Collection</p></div>
  <a class="abs shop-btn" style="left:652px">SHOP NOW</a>
  <div class="abs collection" style="left:765px"><h3>Hamper Collection</h3><p>Shop Hamper Collection</p></div>
  <a class="abs shop-btn" style="left:953px">SHOP NOW</a>

  <section class="abs newsletter">
    <div class="pitch"><strong>Sign up to our newsletter</strong> keep up to date with the latest news, offers and events at The Driftwood!</div>
    <div class="field">YOUR EMAIL
      <svg width="24" height="15" viewBox="0 0 24 15" fill="none" stroke="#fff" stroke-width="1.3"><rect x="1" y="1" width="22" height="13"/><path d="M1 1l11 8 11-8M1 14l8-6M23 14l-8-6"/></svg>
    </div>
  </section>

  <section class="abs perks">
    <div class="perk"><h4>WORLDWIDE DELIVERY</h4><p>Lorem ipsum dolor sit amet, consectetuer<br>adipiscing elit.</p></div>
    <div class="perk"><h4>FREE SHIPPING</h4><p>Lorem ipsum dolor sit amet, consectetuer<br>adipiscing elit.</p></div>
    <div class="perk"><h4>GIFT CERTIFICATE</h4><p>Lorem ipsum dolor sit amet, consectetuer<br>adipiscing elit.</p></div>
    <div class="perk"><h4>QUALITY GUARANTEE</h4><p>Lorem ipsum dolor sit amet, consectetuer<br>adipiscing elit.</p></div>
  </section>

  <nav class="abs footer-links"><a class="current">STORE LOCATOR</a><span>|</span>CATALOGUE<span>|</span>DELIVERY &amp; RETURNS<span>|</span>FAQs<span>|</span>ABOUT US<span>|</span>SITE FEEDBACK</nav>
  <nav class="abs social">FRIENDPAGE<span>|</span>CHIRPLY<span>|</span>CIRCLEO+</nav>
  <div class="abs footer-rule"></div>
  <div class="abs legal">© Company Name &nbsp; | Privacy | Terms &amp; Conditions | Sitemap</div>
  <div class="abs payments"><b>PayMore</b><b>Cardo</b><b>Vantix</b></div>
</div>
</body>
</html>
```